Business card and (possibly) logo

Hi - we need a new business card.
We have an existing logo that we quite like but we are open to options.
We are an architectural firm - we specialize in upmarket residential work and apartment blocks.
We are chasing a business card at present but also want to extensively update our website going forward to attract a much higher level of client / investor / developer.
Our current logo is black, grey and yellow and based on the sun/moon temples in Mexico.
We are open to variations.
We want to communicate professionalism, trust, quality.
Our website is www.korvalstudio.com.au - but note as above - we want to change the website as well to be a lot 'classier' and to appeal to a higher end market.

thanks

Target Market(s)

We are an architect firm - our target market is Developers and builders of high end houses and luxury apartment blocks. Also private home owners wanting to build excellent expensive houses. (ideally over $1m budgets)

Industry/Entity Type

Residential

Requirements
Must have
• Logo
Contact details;
Name
phone, mobile, email, web

```html
<!DOCTYPE html>
<html lang="en">
<head>
<meta charset="utf-8">
<title>Korval Studio – Business Cards</title>
<link href="https://fonts.googleapis.com/css2?family=Saira:wght@400;600&display=swap" rel="stylesheet">
<style>
  :root{
    --page:#ffffff;
    --ink:#161616;
    --rule:#9a9a9a;
    --gold-hi:#fffbe2; --gold-mid:#f2c200; --gold-edge:#c9931c;
    --slate-hi:#ececec; --slate-mid:#a8acb0; --slate-edge:#6d747a;
    --red-hi:#f7a877; --red-mid:#e63422; --red-edge:#d11418;
  }
  *{margin:0;padding:0;box-sizing:border-box}
  html,body{width:1200px;height:1000px;overflow:hidden;background:var(--page)}
  body{position:relative;font-family:"Saira",sans-serif;color:var(--ink)}

  .card{position:absolute;width:510px;height:306px;overflow:hidden}
  .card--front{left:86px}
  .card--back{left:614px}
  .row-1{top:40px}.row-2{top:351px}.row-3{top:661px}

  .card--front.gold{background:radial-gradient(ellipse 260px 210px at 50% 38%,var(--gold-hi) 0%,var(--gold-mid) 60%,var(--gold-edge) 100%)}
  .card--back.gold{background:radial-gradient(ellipse 230px 190px at 26% 30%,var(--gold-hi) 0%,var(--gold-mid) 55%,var(--gold-edge) 100%)}
  .card--front.slate{background:radial-gradient(ellipse 260px 210px at 50% 38%,var(--slate-hi) 0%,var(--slate-mid) 60%,var(--slate-edge) 100%)}
  .card--back.slate{background:radial-gradient(ellipse 230px 190px at 26% 30%,var(--slate-hi) 0%,var(--slate-mid) 55%,var(--slate-edge) 100%)}
  .card--front.red{background:radial-gradient(ellipse 260px 210px at 50% 38%,var(--red-hi) 0%,var(--red-mid) 60%,var(--red-edge) 100%)}
  .card--back.red{background:radial-gradient(ellipse 230px 190px at 26% 30%,var(--red-hi) 0%,var(--red-mid) 55%,var(--red-edge) 100%)}

  .horizon{position:absolute;left:0;top:138px;height:2px;background:var(--rule)}
  .card--front .horizon{right:0}
  .card--back .horizon{width:252px}

  .brand{position:absolute;text-align:center;color:var(--ink);font-weight:600;line-height:1}
  .card--front .brand{left:155px;width:200px;top:150px}
  .card--back .brand{left:62px;width:140px;top:142px}
  .brand__main{display:block;font-size:50px;letter-spacing:1px}
  .brand__sub{display:block;font-size:22px;letter-spacing:2px;margin-top:6px;padding:4px 0 6px;border-top:1.5px solid var(--ink);border-bottom:1.5px solid var(--ink)}
  .card--back .brand__main{font-size:36px}
  .card--back .brand__sub{font-size:15px;margin-top:4px;padding:3px 0 4px}
  .tagline{display:block;font-size:7.5px;letter-spacing:.2px;margin-top:5px;white-space:nowrap}
  .card--back .tagline{font-size:5.5px;margin-top:4px}

  .contact{position:absolute;left:268px;top:102px;font-size:11.5px;line-height:15.5px;font-weight:400}
  .contact__name{font-size:19px;font-weight:400;letter-spacing:.5px;margin-bottom:20px}

  .services{position:absolute;left:0;right:0;top:258px;padding-top:4px;border-top:2px solid var(--rule);text-align:center;font-size:6.4px;line-height:10px;font-weight:600}
</style>
</head>
<body>

<!-- Gold -->
<section class="card card--front gold row-1">
  <div class="horizon"></div>
  <div class="brand"><span class="brand__main">KORVAL</span><span class="brand__sub">STUDIO</span><span class="tagline">ARCHITECTURE | DEVELOPMENT | BUILDING DESIGN</span></div>
</section>
<section class="card card--back gold row-1">
  <div class="horizon"></div>
  <div class="brand"><span class="brand__main">KORVAL</span><span class="brand__sub">STUDIO</span><span class="tagline">ARCHITECTURE | DEVELOPMENT | BUILDING DESIGN</span></div>
  <div class="contact">
    <p class="contact__name">ELIAS MARREN</p>
    <p>Suite 8, 42 - 48 Harbour View Road,</p>
    <p>Coralbay, WA 6087</p>
    <p>PO Box 318 Coralbay WA 6935</p>
    <p>T&nbsp; 1300 61 27 94</p>
    <p>M&nbsp; 0412 555 208</p>
    <p>M&nbsp; 0400 555 617</p>
    <p>W www.korvalstudio.com.au</p>
  </div>
  <div class="services">
    <p>Sketch and Concept Design of your New Home, Extension, Renovation or Development &nbsp;|&nbsp; Drafting of Concept and Construction Drawings &nbsp;|&nbsp; Council</p>
    <p>Approval and Building Licenses &nbsp;|&nbsp; Surveys by Fully Licensed Surveyors &nbsp;|&nbsp; Builders Quotes and Cost Estimates &nbsp;|&nbsp; Structural Design and Documentation &nbsp;|</p>
    <p>Energy Assessment for Building Compliance &nbsp;|&nbsp; Interior and Concept Design &nbsp;|&nbsp; Landscape Design</p>
  </div>
</section>

<!-- Slate -->
<section class="card card--front slate row-2">
  <div class="horizon"></div>
  <div class="brand"><span class="brand__main">KORVAL</span><span class="brand__sub">STUDIO</span><span class="tagline">ARCHITECTURE | DEVELOPMENT | BUILDING DESIGN</span></div>
</section>
<section class="card card--back slate row-2">
  <div class="horizon"></div>
  <div class="brand"><span class="brand__main">KORVAL</span><span class="brand__sub">STUDIO</span><span class="tagline">ARCHITECTURE | DEVELOPMENT | BUILDING DESIGN</span></div>
  <div class="contact">
    <p class="contact__name">ELIAS MARREN</p>
    <p>Suite 8, 42 - 48 Harbour View Road,</p>
    <p>Coralbay, WA 6087</p>
    <p>PO Box 318 Coralbay WA 6935</p>
    <p>T&nbsp; 1300 61 27 94</p>
    <p>M&nbsp; 0412 555 208</p>
    <p>M&nbsp; 0400 555 617</p>
    <p>W www.korvalstudio.com.au</p>
  </div>
  <div class="services">
    <p>Sketch and Concept Design of your New Home, Extension, Renovation or Development &nbsp;|&nbsp; Drafting of Concept and Construction Drawings &nbsp;|&nbsp; Council</p>
    <p>Approval and Building Licenses &nbsp;|&nbsp; Surveys by Fully Licensed Surveyors &nbsp;|&nbsp; Builders Quotes and Cost Estimates &nbsp;|&nbsp; Structural Design and Documentation &nbsp;|</p>
    <p>Energy Assessment for Building Compliance &nbsp;|&nbsp; Interior and Concept Design &nbsp;|&nbsp; Landscape Design</p>
  </div>
</section>

<!-- Red -->
<section class="card card--front red row-3">
  <div class="horizon"></div>
  <div class="brand"><span class="brand__main">KORVAL</span><span class="brand__sub">STUDIO</span><span class="tagline">ARCHITECTURE | DEVELOPMENT | BUILDING DESIGN</span></div>
</section>
<section class="card card--back red row-3">
  <div class="horizon"></div>
  <div class="brand"><span class="brand__main">KORVAL</span><span class="brand__sub">STUDIO</span><span class="tagline">ARCHITECTURE | DEVELOPMENT | BUILDING DESIGN</span></div>
  <div class="contact">
    <p class="contact__name">ELIAS MARREN</p>
    <p>Suite 8, 42 - 48 Harbour View Road,</p>
    <p>Coralbay, WA 6087</p>
    <p>PO Box 318 Coralbay WA 6935</p>
    <p>T&nbsp; 1300 61 27 94</p>
    <p>M&nbsp; 0412 555 208</p>
    <p>M&nbsp; 0400 555 617</p>
    <p>W www.korvalstudio.com.au</p>
  </div>
  <div class="services">
    <p>Sketch and Concept Design of your New Home, Extension, Renovation or Development &nbsp;|&nbsp; Drafting of Concept and Construction Drawings &nbsp;|&nbsp; Council</p>
    <p>Approval and Building Licenses &nbsp;|&nbsp; Surveys by Fully Licensed Surveyors &nbsp;|&nbsp; Builders Quotes and Cost Estimates &nbsp;|&nbsp; Structural Design and Documentation &nbsp;|</p>
    <p>Energy Assessment for Building Compliance &nbsp;|&nbsp; Interior and Concept Design &nbsp;|&nbsp; Landscape Design</p>
  </div>
</section>

</body>
</html>
```